Empresa de tecnología busca diseño de tarjetas de presentación

Se requiere tarjeta de presentación impresa, con los datos de contacto y logo de la empresa. (se adjunta una imagen como referencia, esto no significa que deberá de ser igual)

```html
<!DOCTYPE html>
<html lang="es">
<head>
<meta charset="utf-8">
<title>Nubira TI – Tarjeta de presentación</title>
<link href="https://fonts.googleapis.com/css2?family=Lato:wght@400;700;900&display=swap" rel="stylesheet">
<style>
  :root {
    --green: #76bb21;
    --navy: #0a3d73;
    --white: #ffffff;
    --ink: #2a2a2a;
    --backdrop: #e9e9eb;
    --rule: #d6d9de;
  }
  * { box-sizing: border-box; margin: 0; padding: 0; }
  html, body { width: 1200px; height: 1015px; overflow: hidden; }
  body {
    background: var(--backdrop);
    font-family: "Lato", sans-serif;
    position: relative;
  }
  .card {
    position: absolute;
    width: 640px;
    height: 366px;
    box-shadow: 0 14px 30px rgba(0,0,0,.18);
    overflow: hidden;
  }
  /* Front */
  .card-front { left: 110px; top: 80px; display: flex; }
  .front-half-green { flex: 1; background: var(--green); }
  .front-half-navy { flex: 1; background: var(--navy); }
  .front-brand {
    position: absolute; inset: 0;
    display: flex; align-items: center; justify-content: center;
    color: var(--white); font-weight: 900; font-size: 64px; letter-spacing: 6px;
  }
  /* Back */
  .card-back { left: 450px; top: 540px; background: var(--white); }
  .back-band { position: absolute; left: 0; right: 0; bottom: 0; height: 12px; background: var(--navy); }
  .back-brand {
    position: absolute; left: 48px; top: 160px;
    display: flex; align-items: center; gap: 12px;
    color: var(--navy); font-weight: 900; font-size: 42px; letter-spacing: 4px;
  }
  .back-brand .dot { width: 14px; height: 14px; border-radius: 50%; background: var(--green); }
  .back-divider {
    position: absolute; left: 318px; top: 30px; bottom: 40px; width: 1px;
    background: linear-gradient(to bottom, transparent, var(--rule) 20%, var(--rule) 80%, transparent);
  }
  .contact { position: absolute; left: 340px; top: 42px; right: 20px; color: var(--ink); }
  .contact-name { color: var(--navy); font-weight: 900; font-size: 21px; letter-spacing: .5px; }
  .contact-role { color: var(--green); font-size: 15px; margin-bottom: 14px; }
  .contact-line { display: flex; align-items: center; gap: 8px; font-size: 14.5px; line-height: 24px; }
  .contact-line svg { width: 14px; height: 14px; flex: none; }
  .support-title { color: var(--navy); font-weight: 700; font-size: 15.5px; margin-top: 14px; }
  .icon-navy { fill: var(--navy); }
  .icon-green { fill: var(--green); }
</style>
</head>
<body>

<section class="card card-front">
  <div class="front-half-green"></div>
  <div class="front-half-navy"></div>
  <div class="front-brand">Nubira TI</div>
</section>

<section class="card card-back">
  <div class="back-brand"><span class="dot"></span>Nubira TI</div>
  <div class="back-divider"></div>

  <div class="contact">
    <div class="contact-name">LUCÍA ROMERO</div>
    <div class="contact-role">Gerente Marketing Digital</div>

    <div class="contact-line">
      <svg viewBox="0 0 16 16" class="icon-navy"><path d="M3 2h3l1.5 3.5-2 1.2a8 8 0 0 0 3.8 3.8l1.2-2L14 10v3a1 1 0 0 1-1 1A12 12 0 0 1 2 3a1 1 0 0 1 1-1z"/></svg>
      (55)5550 2841 ext.204
    </div>
    <div class="contact-line">
      <svg viewBox="0 0 16 16" class="icon-navy"><path d="M5 1h6a1 1 0 0 1 1 1v12a1 1 0 0 1-1 1H5a1 1 0 0 1-1-1V2a1 1 0 0 1 1-1zm0 2v9h6V3zm3 10a.8.8 0 1 0 0 .1z"/></svg>
      55 5550 7316
    </div>
    <div class="contact-line">
      <svg viewBox="0 0 16 16" class="icon-navy"><path d="M1 3h14v10H1zm1.5 1.5v.3L8 9l5.5-4.2v-.3zm0 2.2v4.8h11V6.7L8 10.9z"/></svg>
      lucia.romero@nubirati.com
    </div>
    <div class="contact-line">
      <svg viewBox="0 0 16 16" class="icon-navy"><path d="M8 1a5 5 0 0 1 5 5c0 3.5-5 9-5 9S3 9.5 3 6a5 5 0 0 1 5-5zm0 3a2 2 0 1 0 0 4 2 2 0 0 0 0-4z"/></svg>
      Piso 12 Torre Alameda CDMX
    </div>

    <div class="support-title">¿Necesitas levantar un ticket?</div>
    <div class="contact-line">
      <svg viewBox="0 0 16 16" class="icon-green"><path d="M3 2h3l1.5 3.5-2 1.2a8 8 0 0 0 3.8 3.8l1.2-2L14 10v3a1 1 0 0 1-1 1A12 12 0 0 1 2 3a1 1 0 0 1 1-1z"/></svg>
      01 800 5550199
    </div>
    <div class="contact-line">
      <svg viewBox="0 0 16 16" class="icon-green"><path d="M1 3h14v10H1zm1.5 1.5v.3L8 9l5.5-4.2v-.3zm0 2.2v4.8h11V6.7L8 10.9z"/></svg>
      soporte@nubirati.com
    </div>
  </div>

  <div class="back-band"></div>
</section>

</body>
</html>
```